Electronic Letterhead for The Harborline Partners, LLC

I would like to have an electronic letterhead layout using Word for first and second page letterhead using my previously designed logo. The logo was successfully designed by a designer for the Sketch Harbor. I would like to only use the "C" portion of the logo on the second page. I would like the designer that designed my logo to be included in the designers that participate in this competition.

Target Market(s)

My clients are typically governmental entities or financial entities

Industry/Entity Type

Electronic

Font styles to use
Sans Serif

Requirements
Must have
• Utilize existing logo
Nice to have
• Fist and second page letterhead design in electronic format (Word)

```html
<!DOCTYPE html>
<html lang="en">
<head>
<meta charset="utf-8">
<title>The Harborline Partners, LLC – Letterhead</title>
<link rel="stylesheet" href="https://fonts.googleapis.com/css2?family=Tinos&family=Arimo:wght@400;700&display=swap">
<style>
  :root {
    --backdrop: #666666;
    --paper: #ffffff;
    --brand-blue: #0b3a7a;
    --band-blue: #003b80;
    --band-grey: #5a5a5a;
    --watermark: #dfe5ee;
  }
  * { margin: 0; padding: 0; box-sizing: border-box; }
  html, body { width: 1200px; height: 1000px; overflow: hidden; }
  body { background: var(--backdrop); position: relative; }

  .sheet {
    position: absolute;
    top: 91px;
    height: 783px;
    background: var(--paper);
    overflow: hidden;
  }
  .sheet--first { left: 27px; width: 554px; }
  .sheet--second { left: 617px; width: 553px; }

  .brand {
    position: absolute;
    left: 45px;
    top: 39px;
    display: flex;
    align-items: center;
    gap: 8px;
  }
  .brand__dot {
    width: 46px; height: 46px;
    border-radius: 50%;
    background: var(--brand-blue);
  }
  .brand__name {
    font-family: "Tinos", "Times New Roman", serif;
    color: var(--brand-blue);
    font-size: 15px;
    line-height: 15px;
    text-transform: uppercase;
    border-left: 1px solid #9a9a9a;
    padding-left: 4px;
  }
  .brand__name small { font-size: 10px; display: block; line-height: 12px; }
  .brand__name .brand__sub { font-size: 13px; color: #555; }

  .contact {
    position: absolute;
    left: 382px;
    top: 38px;
    list-style: none;
    font-family: "Arimo", Arial, sans-serif;
    font-weight: 700;
    font-size: 8px;
    color: var(--brand-blue);
  }
  .contact li { display: flex; align-items: center; gap: 4px; height: 12px; }
  .contact svg { width: 8px; height: 8px; flex: none; }

  .running-head {
    position: absolute;
    top: 18px;
    left: 0; right: 0;
    text-align: center;
    font-family: "Tinos", "Times New Roman", serif;
    color: var(--brand-blue);
    font-size: 14px;
    text-transform: uppercase;
  }
  .running-head small { font-size: 10px; color: #555; }
  .running-head .running-head__end { font-size: 13px; color: #555; }

  .watermark {
    position: absolute;
    border-radius: 50%;
    background: var(--watermark);
  }
  .sheet--first .watermark { left: 143px; top: 321px; width: 270px; height: 270px; }
  .sheet--second .watermark { left: 158px; top: 339px; width: 236px; height: 236px; }

  .footer-rule {
    position: absolute;
    left: 0; right: 0;
    bottom: 46px;
    height: 4px;
    background: var(--band-grey);
  }
  .footer-band {
    position: absolute;
    left: 0; right: 0;
    bottom: 0;
    height: 38px;
    background: var(--band-blue);
  }
</style>
</head>
<body>

  <section class="sheet sheet--first" aria-label="First page letterhead">
    <div class="brand">
      <span class="brand__dot"></span>
      <p class="brand__name"><small>The</small>Harborline<br><span class="brand__sub">Partners, LLC</span></p>
    </div>

    <ul class="contact">
      <li>
        <svg viewBox="0 0 8 8"><rect width="8" height="8" rx="1" fill="currentColor"/><path d="M2.2 1.6 L3.2 2.8 L2.7 3.4 Q3.4 4.8 4.6 5.3 L5.2 4.8 L6.4 5.8 L5.7 6.6 Q2.8 6.2 1.4 2.4 Z" fill="#fff"/></svg>
        0400 555 018
      </li>
      <li>
        <svg viewBox="0 0 8 8"><rect width="8" height="8" rx="1" fill="currentColor"/><rect x="1.5" y="2.3" width="5" height="3.6" fill="none" stroke="#fff" stroke-width=".7"/><path d="M1.5 2.3 L4 4.3 L6.5 2.3" fill="none" stroke="#fff" stroke-width=".7"/></svg>
        mail@harborline.example
      </li>
      <li>
        <svg viewBox="0 0 8 8"><rect width="8" height="8" rx="1" fill="currentColor"/><circle cx="4" cy="4" r="2.6" fill="none" stroke="#fff" stroke-width=".7"/><path d="M1.4 4 H6.6 M4 1.4 V6.6" stroke="#fff" stroke-width=".6"/></svg>
        www.harborline.example
      </li>
      <li>
        <svg viewBox="0 0 8 8"><rect width="8" height="8" rx="1" fill="currentColor"/><path d="M4 7 L2.2 4.2 A2.1 2.1 0 1 1 5.8 4.2 Z" fill="#fff"/><circle cx="4" cy="3.1" r=".8" fill="currentColor"/></svg>
        PO Box 300 Bayview, NSW, 2999
      </li>
    </ul>

    <div class="watermark" aria-hidden="true"></div>

    <div class="footer-rule" aria-hidden="true"></div>
    <div class="footer-band" aria-hidden="true"></div>
  </section>

  <section class="sheet sheet--second" aria-label="Second page letterhead">
    <p class="running-head"><small>The</small> Harborline <span class="running-head__end">Partners, <small>LLC</small></span></p>

    <div class="watermark" aria-hidden="true"></div>

    <div class="footer-rule" aria-hidden="true"></div>
    <div class="footer-band" aria-hidden="true"></div>
  </section>

</body>
</html>
```